I need a Label design for my copper 71 kombucha brand that is launching soon

I want a label to go on my copper 71 kombucha bottle.
I have a logo image uploaded in the files but I am open to changes to this logo or even a completely New one if you think you can do better. This logo is based on the idea of an s-shaped naga. I particularly like the nagas from temples in luang prabang.
I also want to include the slogan - dare to be delicious.
The label should be some kind of oval at 80mm high by 70mm wide.
The label will go on a clear glass bottle. The kombucha will be visible and comes in different shades of red,yellow and purple.
The word kombucha should be clearly visible.
i want a very colorful, playful label. I'm very keen to see your ideas and I want something original.
Fermented foods and beverages

```html
<!DOCTYPE html>
<html lang="en">
<head>
<meta charset="utf-8">
<title>copper 71 kombucha label</title>
<link rel="stylesheet" href="https://fonts.googleapis.com/css2?family=Josefin+Sans:wght@300;400&family=Roboto+Condensed:wght@400&display=swap">
<style>
  :root {
    --backdrop: #767676;
    --label-white: #ffffff;
    --magenta: #c21b78;
    --charcoal: #58585a;
    --ghost: #e4e4e4;
    --text-white: #ffffff;
  }
  html, body {
    margin: 0;
    padding: 0;
    width: 1200px;
    height: 1200px;
    overflow: hidden;
    background: var(--backdrop);
  }
  .label-artboard {
    display: block;
    width: 1200px;
    height: 1200px;
  }
  .brand-name {
    font-family: "Josefin Sans", sans-serif;
    font-weight: 300;
    fill: var(--charcoal);
  }
  .product-word {
    font-family: "Josefin Sans", sans-serif;
    font-weight: 400;
    fill: var(--text-white);
  }
  .product-word-ghost {
    font-family: "Josefin Sans", sans-serif;
    font-weight: 400;
    fill: var(--ghost);
  }
  .slogan {
    font-family: "Roboto Condensed", sans-serif;
    font-weight: 400;
    fill: var(--text-white);
  }
  .label-sheet { fill: var(--label-white); }
  .diagonal-band { fill: var(--magenta); }
  .brand-dot { fill: var(--magenta); }
  .slogan-bar { fill: var(--charcoal); }
</style>
</head>
<body>
<svg class="label-artboard" viewBox="0 0 960 960" xmlns="http://www.w3.org/2000/svg">
  <defs>
    <clipPath id="label-edge">
      <rect x="148" y="102" width="662" height="756"/>
    </clipPath>
  </defs>

  <rect class="label-sheet" x="148" y="102" width="662" height="756"/>

  <g clip-path="url(#label-edge)">
    <!-- faint echo of the product word -->
    <g transform="translate(300,900) rotate(-14.2)">
      <text class="product-word-ghost" x="0" y="-95" font-size="165" textLength="445" lengthAdjust="spacingAndGlyphs">kom</text>
      <text class="product-word-ghost" x="-20" y="0" font-size="165" textLength="560" lengthAdjust="spacingAndGlyphs">bucha</text>
    </g>

    <polygon class="diagonal-band" points="148,490 810,322 810,720 265,858 148,858"/>

    <g transform="translate(250,612) rotate(-14.2)">
      <text class="product-word" x="0" y="0" font-size="168" textLength="445" lengthAdjust="spacingAndGlyphs">kom</text>
      <text class="product-word" x="-18" y="95" font-size="168" textLength="560" lengthAdjust="spacingAndGlyphs">bucha</text>
    </g>

    <g transform="translate(280,792) rotate(-14.2)">
      <rect class="slogan-bar" x="0" y="-52" width="455" height="52"/>
      <text class="slogan" x="22" y="-13" font-size="36">dare to be delicious</text>
    </g>
  </g>

  <circle class="brand-dot" cx="480" cy="196" r="42"/>
  <text class="brand-name" x="480" y="318" font-size="58" text-anchor="middle">copper 71</text>
</svg>
</body>
</html>
```